drink bottle label

Our drink is called VELMORA zi, a 2000 year old Asian formula for a fermented green tea drink. Flavored with organic ginger juice, cinnamon and lime. Very tasty and refreshing, good for sports recovery, digestion,liver detox,overall health and vitality. Naturally fermented creating a- no sugar, low GI, salt,-fat and gluten free- fizzy drink alternative to soft drink, sports drinks or beer. The bottle is a brown 330ml long neck bottle. For the diet and health conscious individual. We would like the label to be upmarket for restaurants & trendy organic food suppliers.
Updates

Reason: Take more time to get the best result

The bottle is brown. Try using black-gold-silver-white for the subject in a white or silver border

Target Market(s)

Upmarket, for restaurant & trendy organic food supplies.Sophisticated Health conscious people who don't want high sugar, caffeine drinks.

Industry/Entity Type

Health

Requirements
Must have
• The drink name and registered brand is" VELMORA zi."
Must feature PROBIOTICS & ENZYMES for detox.No artificial preservatives or colours. 100% Organic & raw living culture.Low GI low calorie- no cane sugar, no salt-
- no lactose, Coeliac -diabetic & vegan friendly. Ginger Brew.
Nice to have
• tastes great-revitalize- 330ml brown bottle

```html
<!DOCTYPE html>
<html lang="en">
<head>
<meta charset="utf-8">
<title>Velmora Zi – Bottle Label</title>
<link rel="stylesheet" href="https://fonts.googleapis.com/css2?family=Questrial&family=Alfa+Slab+One&family=Didact+Gothic&display=swap">
<style>
  :root{
    --page:#efefef;
    --gold-dark:#9a6224;
    --gold-mid:#c58a3e;
    --gold-light:#f3e2a6;
    --silver-light:#f4f4f4;
    --silver-mid:#c9c9cb;
    --silver-dark:#8e8f92;
    --green:#1f6b1c;
    --green-dark:#12470f;
    --yellow:#f3e81a;
    --brown:#7a4a1c;
    --ink:#222;
    --copy:#ffffff;
  }
  *{margin:0;padding:0;box-sizing:border-box}
  html,body{width:1200px;height:1000px;overflow:hidden}
  body{
    background:radial-gradient(ellipse at 50% 45%, #fafafa 0%, var(--page) 70%, #e2e2e2 100%);
    font-family:"Questrial", sans-serif;
    position:relative;
  }
  .label{
    position:absolute;left:40px;top:256px;width:1121px;height:489px;
    background:linear-gradient(90deg,var(--gold-dark),var(--gold-mid) 20%,var(--gold-light) 50%,var(--gold-mid) 80%,var(--gold-dark));
    padding:9px;
  }
  .label__face{
    position:relative;width:100%;height:100%;
    background:linear-gradient(90deg,var(--silver-mid) 0%,var(--silver-light) 22%,#fff 40%,var(--silver-mid) 62%,var(--silver-dark) 82%,var(--silver-mid) 100%);
    overflow:hidden;
  }
  .story{
    position:absolute;left:11px;top:66px;width:136px;
    font-family:"Didact Gothic", sans-serif;font-size:9.6px;line-height:14.4px;color:var(--copy);
  }
  .distributor{
    position:absolute;left:44px;top:361px;font-family:"Didact Gothic", sans-serif;
    font-size:9.6px;color:var(--brown);
  }
  .claim{
    position:absolute;width:100px;height:100px;border-radius:50%;
    background:radial-gradient(circle,#fff 58%,var(--gold-light) 62%,var(--gold-mid) 70%,var(--gold-dark) 76%,#fff 80%,#fff 100%);
    display:flex;align-items:center;justify-content:center;text-align:center;
    font-size:12.5px;line-height:15px;color:var(--brown);font-weight:bold;left:174px;
  }
  .claim span{display:block;width:70px}
  .splash{
    position:absolute;left:368px;top:6px;width:380px;height:282px;border-radius:48% 52% 40% 44%;
    background:radial-gradient(ellipse at 45% 40%, rgba(243,232,26,.85) 0%, rgba(232,222,90,.55) 40%, rgba(160,170,60,.25) 65%, rgba(255,255,255,0) 75%);
  }
  .brand{
    position:absolute;left:368px;top:160px;width:380px;text-align:center;
    font-family:"Alfa Slab One", serif;font-size:52px;color:var(--green);letter-spacing:1px;
  }
  .volume{position:absolute;left:720px;top:297px;font-size:13px;color:var(--ink)}
  .suitability{
    position:absolute;left:260px;width:600px;text-align:center;color:var(--ink);
  }
  .suitability--diet{top:319px;font-size:21px;letter-spacing:.5px}
  .suitability--free{top:355px;font-size:15px;word-spacing:10px}
  .suitability--low{top:377px;font-size:14px}
  .box{display:inline-block;width:13px;height:13px;vertical-align:-1px;margin:0 2px}
  .flavour{
    position:absolute;left:260px;width:600px;text-align:center;font-family:"Alfa Slab One", serif;
    color:var(--yellow);-webkit-text-stroke:1.5px var(--green-dark);paint-order:stroke fill;
  }
  .flavour--notes{top:402px;font-size:20px;word-spacing:8px}
  .flavour--name{top:430px;font-size:33px;letter-spacing:1px}
  .nutrition{
    position:absolute;left:853px;top:23px;width:214px;height:302px;background:#fff;
    padding:6px 8px;font-family:"Didact Gothic", sans-serif;font-size:9.8px;color:var(--ink);
  }
  .nutrition h3{font-size:11.5px;font-weight:bold;border-bottom:1px solid #000;padding-bottom:1px}
  .nutrition .row{display:flex;justify-content:space-between;border-bottom:1px solid #999;padding:1.4px 0}
  .nutrition .row--indent{padding-left:12px}
  .nutrition .row--thick{border-bottom:4px solid #000}
  .nutrition .row--heavy{border-bottom:2px solid #000}
  .nutrition .row--right{justify-content:flex-end}
  .nutrition b{font-weight:bold}
  .nutrition .note{padding-top:4px;line-height:12px}
  .disposal{position:absolute;left:995px;top:361px;display:flex;gap:12px}
  .disposal span{width:16px;height:16px;border-radius:50%;background:var(--green)}
</style>
</head>
<body>
  <section class="label" aria-label="Velmora Zi bottle label, flat">
    <div class="label__face">
      <p class="story">Our drink is called VELMORA zi, a 2000 year old Asian formula for a fermented green tea drink. Flavored with organic ginger juice, cinnamon and lime. Very tasty and refreshing, good for sports recovery, digestion, liver detox, overall health and vitality. Naturally fermented creating a - no sugar, low GI, salt, fat and gluten free- fizzy drink alternative to soft drink, sports drinks or beer.</p>
      <p class="distributor">Distributed by:</p>

      <div class="claim" style="top:51px"><span>Probiotics &amp; Enzymes For inner health</span></div>
      <div class="claim" style="top:165px"><span>No artificial preservatives or colours</span></div>
      <div class="claim" style="top:272px"><span>Glucaric Acid for detox</span></div>

      <div class="splash" role="img" aria-label="Illustration of a yellow-green tea splash with green tea leaves, cinnamon sticks, ginger root and a lime slice"></div>
      <div class="brand">Velmora Zi</div>
      <div class="volume">330ml</div>

      <p class="suitability suitability--diet">Coeliac<svg class="box" viewBox="0 0 13 13"><rect x=".5" y=".5" width="12" height="12" fill="none" stroke="#222"/><path d="M3 7l2.5 2.5L10.5 3" fill="none" stroke="#222" stroke-width="1.3"/></svg> Diabetic<svg class="box" viewBox="0 0 13 13"><rect x=".5" y=".5" width="12" height="12" fill="none" stroke="#222"/><path d="M3 7l2.5 2.5L10.5 3" fill="none" stroke="#222" stroke-width="1.3"/></svg> Vegan<svg class="box" viewBox="0 0 13 13"><rect x=".5" y=".5" width="12" height="12" fill="none" stroke="#222"/><path d="M3 7l2.5 2.5L10.5 3" fill="none" stroke="#222" stroke-width="1.3"/></svg></p>
      <p class="suitability suitability--free"><svg class="box" viewBox="0 0 13 13"><rect x=".5" y=".5" width="12" height="12" fill="none" stroke="#222"/><path d="M3 3l7 7M10 3l-7 7" stroke="#222"/></svg>No&nbsp;Glucose <svg class="box" viewBox="0 0 13 13"><rect x=".5" y=".5" width="12" height="12" fill="none" stroke="#222"/><path d="M3 3l7 7M10 3l-7 7" stroke="#222"/></svg>No&nbsp;Lactose <svg class="box" viewBox="0 0 13 13"><rect x=".5" y=".5" width="12" height="12" fill="none" stroke="#222"/><path d="M3 3l7 7M10 3l-7 7" stroke="#222"/></svg>No&nbsp;Gluten <svg class="box" viewBox="0 0 13 13"><rect x=".5" y=".5" width="12" height="12" fill="none" stroke="#222"/><path d="M3 3l7 7M10 3l-7 7" stroke="#222"/></svg>No&nbsp;Salt</p>
      <p class="suitability suitability--low">Low Calorie, Low GI</p>

      <p class="flavour flavour--notes">ginger lime cinnamon</p>
      <p class="flavour flavour--name">ORIGINAL</p>

      <div class="nutrition">
        <h3>Nutrition Facts</h3>
        <div class="row"><span>Serving Size 1/2 Cup (85g)</span></div>
        <div class="row"><span>Serving Per Container About 4</span></div>
        <div class="row"><span>Amount Per Serving</span></div>
        <div class="row row--heavy"><span><b>Calories</b> 160</span><span><b>Calories from Fat</b> 120</span></div>
        <div class="row row--right"><span>% Daily Value*</span></div>
        <div class="row"><span><b>Total Fat</b> 9g</span><span>14%</span></div>
        <div class="row row--indent"><span>Saturated Fat 5g</span><span>25%</span></div>
        <div class="row row--indent"><span>Trans Fat 0g</span><span></span></div>
        <div class="row row--indent"><span>Cholesterol 30mg</span><span>10%</span></div>
        <div class="row row--indent"><span>Sodium 30mg</span><span>1%</span></div>
        <div class="row"><span><b>Total Carbohydrate</b> 18g</span><span>6%</span></div>
        <div class="row"><span>Dietary Fiber 0g</span><span>0%</span></div>
        <div class="row"><span>Sugars 16g</span></div>
        <div class="row row--thick"><span><b>Protein</b> 2g</span></div>
        <div class="row"><span>VitaminA 6%</span><span style="width:90px">• VitaminC 2%</span></div>
        <div class="row"><span>Calcium 6%</span><span style="width:90px">• Iron 0%</span></div>
        <p class="note">* Percent Daily Values are based on a 2,000 calorie diet.</p>
      </div>

      <div class="disposal" aria-hidden="true"><span></span><span></span></div>
    </div>
  </section>
</body>
</html>
```